KORU product web page

We need a new web design for our KORU product page. You can find more information about the project on the current web site - www.koru-example.io

What we need from a new design (uncoded):
- landing pages + template
- all information on one page
- the design should be focused on the product - light bulb + app
- web site should be with some dynamics like a background with parallax effect in the current version
- fonts should be chosen
- a number of illustrations should be designed

Here is schema for a new design: https://files.example-share.net/drawings/d/7Qm2Lr9Xk4Pz8Wn3Ty6Vb1Hc5Jd0Fg2Ks4Na/edit

Here is a document with all texts for a new design: https://files.example-share.net/document/d/3Zt8Mp1Rw6Yc9Lk2Hs5Gv0Bn4Xq7Df3Ju8Pe/edit

Illustrations to use:
v1 - https://files.example-share.net/folder?id=4Kp7Tr2Wn9Qs5Lm1Zx8Cv3Bd&share=1
v2 - https://files.example-share.net/folder?id=4Kp7Tr2Wn9Qs6Hy3Rf0Gj5Mk&share=1

iOS screens: https://files.example-share.net/folder?id=9Vd2Ls6Nq1Xw8Pt4Jh7Ec3Ra&share=1

KORU logo: https://files.example-share.net/folder?id=4Kp7Tr2Wn9Qs2Yb6Uc8Fz0Ow&share=1
Updates

I forgot to add the definition text "KORU - is.." to the document with texts. Sorry, my mistake.

Target Market(s)

25-45 year old adults who are interested in "smart" devices for their health.

Industry/Entity Type

Google

Colors

Designer to choose colors to be used in the design.

Requirements
Must have
• - landing pages + template
- fonts should be chosen

```html
<!DOCTYPE html>
<html lang="en">
<head>
<meta charset="utf-8">
<title>KORU — Smart Light Bulb</title>
<link href="https://fonts.googleapis.com/css2?family=Lato:wght@300;400;700;900&display=swap" rel="stylesheet">
<style>
  :root {
    --brand-orange: #f26a30;
    --hero-orange: #f4824f;
    --band-peach: #fbc1a9;
    --footer-orange: #dc7048;
    --footer-text: #f6b08f;
    --white: #ffffff;
    --ink: #111111;
    --dot-muted: rgba(255, 255, 255, 0.55);
  }
  * { box-sizing: border-box; margin: 0; padding: 0; }
  html, body {
    width: 1200px; height: 1000px; overflow: hidden;
    font-family: "Lato", Arial, sans-serif;
    background: var(--hero-orange);
  }
  .page { position: relative; width: 1200px; height: 1000px; }

  .header-band {
    position: absolute; left: 0; top: 0; width: 1200px; height: 120px;
    background: var(--band-peach);
  }
  .nav-bar {
    position: absolute; left: 0; top: 30px; width: 1200px; height: 60px;
    background: var(--white);
  }
  .brand-badge {
    position: absolute; left: 141px; top: 20px; width: 80px; height: 80px;
    border-radius: 50%; background: var(--brand-orange);
    display: flex; align-items: center; justify-content: center;
    color: var(--white); font-weight: 900; font-size: 15px; letter-spacing: 1px;
  }
  .main-nav {
    position: absolute; top: 46px; right: 140px;
    display: flex; gap: 53px; list-style: none;
  }
  .main-nav a {
    font-size: 23px; letter-spacing: 4.2px; color: var(--ink);
    text-decoration: none; line-height: 28px;
  }
  .main-nav a.is-accent { color: var(--brand-orange); font-weight: 700; }

  .hero {
    position: absolute; left: 0; top: 120px; width: 1200px; height: 841px;
    background: var(--hero-orange); color: var(--white); text-align: center;
  }
  .hero-wordmark {
    position: absolute; left: 0; top: 212px; width: 1200px;
    font-size: 128px; font-weight: 900; letter-spacing: 14px; line-height: 130px;
  }
  .hero-title {
    position: absolute; left: 0; top: 382px; width: 1200px;
    font-size: 28px; font-weight: 700; letter-spacing: 6.2px; line-height: 34px;
  }
  .hero-subtitle {
    position: absolute; left: 0; top: 468px; width: 1200px;
    font-size: 20px; font-weight: 300; letter-spacing: 4.2px; line-height: 24px;
  }
  .hero-button {
    position: absolute; left: 471px; top: 557px; width: 258px; height: 60px;
    border: 4px solid var(--white);
    display: flex; align-items: center; justify-content: center;
    font-size: 22px; font-weight: 700; letter-spacing: 4px; color: var(--white);
    text-decoration: none;
  }

  .section-dots {
    position: absolute; left: 20px; top: 459px;
    display: flex; flex-direction: column; gap: 15px; list-style: none;
  }
  .section-dots li {
    width: 15px; height: 15px; border-radius: 50%; background: var(--dot-muted);
  }
  .section-dots li.is-active { background: var(--white); }

  .site-footer {
    position: absolute; left: 0; top: 961px; width: 1200px; height: 39px;
    background: var(--footer-orange); color: var(--footer-text);
  }
  .footer-link {
    position: absolute; left: 141px; top: 11px;
    font-size: 14px; font-weight: 700; color: var(--footer-text); text-decoration: none;
  }
  .footer-copy {
    position: absolute; right: 147px; top: 12px;
    display: flex; align-items: center; gap: 10px; font-size: 11px;
  }
  .footer-copy .footer-brand { font-size: 17px; font-weight: 900; letter-spacing: 2px; }
</style>
</head>
<body>
<div class="page">
  <header>
    <div class="header-band"></div>
    <div class="nav-bar"></div>
    <div class="brand-badge">KORU</div>
    <ul class="main-nav">
      <li><a class="is-accent" href="#">PRE-ORDER</a></li>
      <li><a href="#">BLOG</a></li>
      <li><a href="#">CONTACTS</a></li>
      <li><a href="#">RU</a></li>
    </ul>
  </header>

  <main class="hero">
    <div class="hero-wordmark">KORU</div>
    <h1 class="hero-title">KORU IS THE RIGHT LIGHTING DESIGNED<br>ESPECIALY FOR YOUR HEALTH AND COMFORT</h1>
    <p class="hero-subtitle">A SMART TRUE COLOR BLUETOOTH ENABLED LED LIGHT BULB.</p>
    <a class="hero-button" href="#">LEARN MORE</a>
  </main>

  <ul class="section-dots">
    <li class="is-active"></li><li></li><li></li><li></li><li></li><li></li>
  </ul>

  <footer class="site-footer">
    <a class="footer-link" href="#">CONTACTS</a>
    <div class="footer-copy"><span>COPYRIGHT ©</span><span class="footer-brand">KORU</span></div>
  </footer>
</div>
</body>
</html>
```